Poster Design For Obstacle Run

Design a poster for the Crow Ridge Obstacle run.
Text: Crow Ridge Obstacle Run. May 12th, 2018. Sittard. www.crowridgedash.nl. I have added a lot of pictures.
Furthermore, the logo should be included. As an example I included a poster from the ironbark race that we really like (ironbark team challenge) and also. Feel free to take a look at our website for inspiration: www.crowridgedash.nl

```html
<!DOCTYPE html>
<html lang="en">
<head>
<meta charset="utf-8">
<title>Crow Ridge Obstacle Run – Poster</title>
<link rel="stylesheet" href="https://fonts.googleapis.com/css2?family=Oswald:wght@400;500;700&display=swap">
<style>
  :root {
    --page-bg: #e9e9e6;
    --poster-black: #0b0b0b;
    --run-orange: #e8521c;
    --text-white: #ffffff;
    --mud-dark: #3a2f27;
    --mud-mid: #6b5a4c;
    --shirt-orange: #b5451f;
    --concrete: #8a8580;
  }
  * { box-sizing: border-box; margin: 0; padding: 0; }
  html, body {
    width: 1200px; height: 873px; overflow: hidden;
    background: var(--page-bg);
  }
  .poster {
    position: absolute; left: 365px; top: 30px;
    width: 470px; height: 813px;
    background: var(--poster-black);
    overflow: hidden;
    font-family: "Oswald", "Arial Narrow", sans-serif;
    box-shadow: 0 6px 24px rgba(0,0,0,.25);
  }
  .hero-photo {
    position: absolute; left: 0; top: 0; width: 100%; height: 470px;
    background:
      radial-gradient(ellipse at 78% 40%, var(--shirt-orange) 0%, rgba(181,69,31,0.6) 25%, transparent 50%),
      linear-gradient(150deg, #a8a29a 0%, var(--concrete) 30%, var(--mud-mid) 55%, var(--mud-dark) 80%, var(--poster-black) 100%);
  }
  .mud-splatter {
    position: absolute; left: 0; bottom: 0; width: 100%; height: 95px;
    background: linear-gradient(180deg, var(--poster-black) 0%, #3b3632 45%, #8e8780 100%);
  }
  .title-block {
    position: absolute; left: 90px; top: 500px;
  }
  .city {
    position: absolute; left: 50px; top: 505px;
    width: 150px; height: 30px;
    transform-origin: left top;
    transform: translate(0, 150px) rotate(-90deg);
    color: var(--text-white); font-weight: 700; font-size: 27px;
    letter-spacing: 1px; line-height: 30px;
  }
  .event-name {
    color: var(--text-white); font-weight: 700; font-size: 66px;
    line-height: 74px; text-transform: uppercase; white-space: nowrap;
  }
  .event-type {
    color: var(--run-orange); font-weight: 700; font-size: 50px;
    line-height: 56px; text-transform: uppercase; white-space: nowrap;
  }
  .event-date {
    position: absolute; left: 105px; top: 648px;
    color: var(--text-white); font-weight: 700; font-size: 35px; line-height: 40px;
    white-space: nowrap;
  }
  .event-url {
    position: absolute; left: 107px; top: 690px;
    color: var(--text-white); font-weight: 400; font-size: 16px;
    letter-spacing: 3px; text-transform: uppercase;
  }
  .brand-mark {
    position: absolute; left: 14px; top: 662px;
    display: flex; align-items: center; gap: 5px;
    color: var(--run-orange); font-weight: 500; font-size: 13px;
    text-transform: uppercase; white-space: nowrap;
  }
  .brand-dot {
    width: 9px; height: 9px; border-radius: 50%; background: var(--run-orange);
  }
</style>
</head>
<body>
  <main class="poster">
    <div class="hero-photo" role="img" aria-label="Close-up photo of a mud-covered runner in an orange shirt pulling a rope up a wooden wall"></div>
    <div class="city">Sittard</div>
    <div class="title-block">
      <h1 class="event-name">Crow Ridge</h1>
      <h2 class="event-type">Obstacle Run</h2>
    </div>
    <div class="brand-mark"><span class="brand-dot"></span>Crow Ridge</div>
    <p class="event-date">May 12th, 2018</p>
    <p class="event-url">www.crowridgedash.nl</p>
    <div class="mud-splatter" role="img" aria-label="Dark mud splatter texture along the bottom edge"></div>
  </main>
</body>
</html>
```